Unique & Creative Business Card for Lumivaleta

Would you please create a unique design that is soft and appealing to people who seek to raise vibrational energy for themselves, for animals (domestic or wild), or for the environment.

Optional: Elements could include, landscapes, wild animals, feathers, vibrational patterns, the elements (Earth, water, fire, air and space). Images that are calming.

With Thanks!

Target Market(s)

People and businesses who are into the environment, animal welfare, alternative health.

Contact Information for Business Card

Moira Tess
Energist
mt@lumivaleta.example
lumivaleta.example

Requirements
Must have
• Lumivaleta logo (attached)
Symbols that represent our main services: Natural environment, animal, human and energy.
Our strapline ‘Achieving Vibrational Equilibrium’
Nice to have
• Clear and easy to read
Colours based on nature/soft colours

```html
<!DOCTYPE html>
<html lang="en">
<head>
<meta charset="utf-8">
<title>Lumivaleta Business Card</title>
<link rel="stylesheet" href="https://fonts.googleapis.com/css2?family=Montserrat:wght@400;500&family=Playball&display=swap">
<style>
  :root {
    --page-bg: #ecebee;
    --lavender: #c9bdd6;
    --lavender-deep: #b7a9c8;
    --lavender-mist: #ddd5e6;
    --card-white: #fbfbfc;
    --purple-text: #8a6f9e;
    --grey-text: #7c7c80;
    --ring-blue: #5f8fc4;
    --brand-navy: #3e5a92;
    --dot-tone: rgba(255,255,255,0.55);
    --dot-tone-light: rgba(190,180,205,0.35);
  }
  * { box-sizing: border-box; margin: 0; padding: 0; }
  html, body { width: 1200px; height: 833px; overflow: hidden; }
  body {
    background: var(--page-bg);
    display: flex;
    align-items: center;
    justify-content: center;
    gap: 40px;
    font-family: "Montserrat", sans-serif;
  }
  .card {
    position: relative;
    width: 540px;
    height: 309px;
    border-radius: 4px;
    overflow: hidden;
    box-shadow: 0 10px 28px rgba(60,40,80,0.16);
  }
  .card--front {
    background: linear-gradient(135deg, var(--lavender) 0%, var(--lavender-mist) 55%, var(--lavender-deep) 100%);
  }
  .card--back { background: var(--card-white); }

  .wave-pattern { position: absolute; border-radius: 50%; }
  .card--front .wave-pattern--top {
    top: -120px; right: -90px; width: 340px; height: 260px;
    background: radial-gradient(ellipse at center, var(--dot-tone) 0%, transparent 70%);
  }
  .card--front .wave-pattern--bottom {
    bottom: -130px; left: -80px; width: 360px; height: 270px;
    background: radial-gradient(ellipse at center, var(--dot-tone) 0%, transparent 70%);
  }
  .card--back .wave-pattern--top {
    top: -110px; right: -60px; width: 380px; height: 240px;
    background: radial-gradient(ellipse at center, var(--dot-tone-light) 0%, transparent 70%);
  }

  .brand-mark {
    position: absolute;
    display: flex;
    flex-direction: column;
    align-items: center;
    justify-content: center;
    gap: 6px;
  }
  .brand-mark__circle {
    border: 3px solid var(--ring-blue);
    border-radius: 50%;
    background: rgba(236,230,242,0.85);
    display: flex;
    align-items: center;
    justify-content: center;
  }
  .brand-mark__name {
    color: var(--brand-navy);
    font-weight: 500;
    letter-spacing: 0.06em;
    text-transform: uppercase;
  }
  .card--front .brand-mark { inset: 0; }
  .card--front .brand-mark__circle { width: 170px; height: 170px; }
  .card--front .brand-mark__name { font-size: 19px; }

  .card--back .brand-mark { left: 40px; top: 54px; width: 150px; }
  .card--back .brand-mark__circle { width: 118px; height: 118px; }
  .card--back .brand-mark__name { font-size: 13px; }

  .brand-wordmark {
    position: absolute;
    left: 32px; bottom: 36px;
    display: flex; align-items: center; gap: 12px;
    color: var(--purple-text);
    font-size: 11px;
    letter-spacing: 0.6em;
    text-transform: uppercase;
  }
  .brand-wordmark__bar { width: 16px; height: 3px; background: var(--purple-text); }

  .contact {
    position: absolute;
    right: 44px; top: 92px;
    width: 270px;
  }
  .contact__name {
    font-family: "Playball", cursive;
    color: var(--purple-text);
    font-size: 40px;
    line-height: 1;
  }
  .contact__role {
    display: inline-block;
    margin-top: 4px;
    padding-bottom: 5px;
    border-bottom: 2px solid var(--purple-text);
    color: var(--grey-text);
    font-size: 12px;
    letter-spacing: 0.32em;
    text-transform: uppercase;
  }
  .contact__list { list-style: none; margin-top: 12px; }
  .contact__item {
    display: flex; align-items: center; gap: 10px;
    color: var(--grey-text);
    font-size: 15px;
    margin-bottom: 6px;
  }
  .contact__icon { width: 15px; height: 15px; flex: none; }
</style>
</head>
<body>

  <section class="card card--front" aria-label="Card front">
    <div class="wave-pattern wave-pattern--top" role="img" aria-label="Soft dotted vibrational wave pattern"></div>
    <div class="wave-pattern wave-pattern--bottom" role="img" aria-label="Soft dotted vibrational wave pattern"></div>
    <div class="brand-mark">
      <div class="brand-mark__circle">
        <span class="brand-mark__name">Lumivaleta</span>
      </div>
    </div>
  </section>

  <section class="card card--back" aria-label="Card back">
    <div class="wave-pattern wave-pattern--top" role="img" aria-label="Soft dotted vibrational wave pattern"></div>

    <div class="brand-mark">
      <div class="brand-mark__circle">
        <span class="brand-mark__name">Lumivaleta</span>
      </div>
    </div>

    <div class="brand-wordmark">
      <span class="brand-wordmark__bar"></span>
      <span>Lumivaleta</span>
      <span class="brand-wordmark__bar"></span>
    </div>

    <div class="contact">
      <p class="contact__name">Moira Tess</p>
      <p class="contact__role">Energist</p>
      <ul class="contact__list">
        <li class="contact__item">
          <svg class="contact__icon" viewBox="0 0 16 16" aria-hidden="true">
            <rect x="1" y="3" width="14" height="10" rx="1" fill="#7c7c80"/>
            <path d="M1.5 3.5 L8 9 L14.5 3.5" fill="none" stroke="#fbfbfc" stroke-width="1.3"/>
          </svg>
          <span>mt@lumivaleta.example</span>
        </li>
        <li class="contact__item">
          <svg class="contact__icon" viewBox="0 0 16 16" aria-hidden="true">
            <g fill="none" stroke="#7c7c80" stroke-width="1.2">
              <circle cx="8" cy="8" r="6.5"/>
              <ellipse cx="8" cy="8" rx="2.8" ry="6.5"/>
              <line x1="1.5" y1="8" x2="14.5" y2="8"/>
              <line x1="2.5" y1="4.8" x2="13.5" y2="4.8"/>
              <line x1="2.5" y1="11.2" x2="13.5" y2="11.2"/>
            </g>
          </svg>
          <span>lumivaleta.example</span>
        </li>
      </ul>
    </div>
  </section>

</body>
</html>
```